Family Farm Business Requires Flyer for local CSA retail sales and local advertising

We need a flyer design for our small farm to help promote our CSA business. A CSA is when someone pre-pays for a summer's worth of produce, fruit, and eggs that are raised on our farm. They receive a weekly box of produce and essentially they buy a small share of the summer's bounty. We had a logo designed by someone here on pixel hive so we would like the flyer to include the colors of the logo. The final design should reflect the different options for people the choose and then invite them to sign up to be a CSA Customer.

Target Market(s)

Busy families and moms who are limited in time to buy groceries or healthy food or produce. People who are passionate about local food and local produce.

Industry/Entity Type

Advertising

Font styles to use
Decorative
Script

Requirements
Must have
• Our logo, our farm information (website, social media, location) and contact info as well as the various options to choose from for our CSA farm share. I also included a picture of our business card so it would be good if it matched the colors/style of our card. Also the flyer will be printed on 8.5 x 11 paper and it will be double sided.

```html
<!DOCTYPE html>
<html lang="en">
<head>
<meta charset="utf-8">
<title>Maple Hollow Farm – Summer CSA</title>
<link href="https://fonts.googleapis.com/css2?family=Parisienne&family=Dancing+Script:wght@500;700&family=Kaushan+Script&family=Arimo&display=swap" rel="stylesheet">
<style>
  :root {
    --green: #3cb54a;
    --lime: #7ee01c;
    --leaf: #2fb24c;
    --orange: #fdb813;
    --red: #ed1c24;
    --ink: #1a1a1a;
    --white: #ffffff;
  }
  * { margin: 0; padding: 0; box-sizing: border-box; }
  html, body { width: 851px; height: 1200px; overflow: hidden; background: var(--white); }
  .flyer {
    position: relative; width: 851px; height: 1200px;
    background: var(--white); border: 1px solid var(--ink);
    font-family: "Dancing Script", cursive; color: var(--ink);
  }
  .abs { position: absolute; }

  /* brand */
  .brand { left: 52px; top: 70px; width: 150px; text-align: center; }
  .brand-dot { width: 70px; height: 70px; border-radius: 50%; background: var(--green); margin: 0 auto 14px; }
  .brand-name { font-weight: 700; font-size: 38px; line-height: 1.0; color: var(--green); }
  .tagline { left: 12px; top: 300px; font-size: 24px; font-weight: 700; color: var(--green); white-space: nowrap; }

  /* header */
  .frame-top { left: 272px; top: 21px; width: 576px; height: 10px; background: var(--orange); }
  .frame-side { left: 838px; top: 21px; width: 10px; height: 150px; background: var(--orange); }
  .title { left: 292px; top: 30px; font-family: "Parisienne", cursive; font-size: 86px; line-height: 1; color: var(--green); white-space: nowrap; }

  .photo { top: 168px; width: 130px; height: 156px; border: 5px solid var(--green); }
  .photo.alt { border-color: var(--orange); }
  .photo-veg { left: 262px; background: linear-gradient(160deg, #b9d48a, #4f8a2c 55%, #c63a2a); }
  .photo-apple { left: 413px; background: linear-gradient(160deg, #f0a23c, #c4281c 60%, #8a1a12); }
  .photo-greens { left: 564px; background: linear-gradient(160deg, #d7f0b8, #5fae3a 55%, #2f6d22); }
  .photo-eggs { left: 716px; background: linear-gradient(160deg, #f1d2b0, #c98a58 55%, #8a5a36); }

  .rule { left: 4px; top: 339px; width: 844px; height: 7px; background: var(--orange); }

  /* about + offer */
  .about { left: 4px; top: 352px; width: 844px; height: 274px; background: var(--orange); }
  .about-list { left: 28px; top: 365px; list-style: none; font-size: 30px; line-height: 41px; font-weight: 500; white-space: nowrap; }
  .offer {
    left: 532px; top: 358px; width: 316px; height: 266px;
    background: var(--red); border: 6px solid var(--white); color: var(--white);
    font-family: "Kaushan Script", cursive; text-align: center;
  }
  .offer-num { left: 16px; top: 18px; font-size: 118px; line-height: 1; }
  .offer-weeks { left: 130px; top: 22px; font-size: 44px; line-height: 44px; text-align: left; }
  .offer-delivery { left: 0; width: 100%; top: 152px; font-size: 34px; }
  .offer-dates { left: 0; width: 100%; top: 200px; font-size: 31px; }
  .offer sup { font-size: 16px; }

  /* seasonal */
  .season { left: 4px; top: 636px; width: 844px; height: 252px; background: var(--lime); }
  .season-head { left: 4px; width: 844px; top: 644px; text-align: center; font-size: 34px; font-weight: 700; }
  .season-row { left: 30px; font-size: 20px; font-weight: 500; white-space: nowrap; }
  .month { display: inline-block; width: 86px; }

  /* fruit */
  .fruit { left: 4px; top: 896px; width: 844px; height: 118px; background: var(--red); color: var(--white); text-align: center; }
  .fruit-head { left: 0; width: 100%; top: 8px; font-size: 33px; font-weight: 700; }
  .fruit-line { left: 0; width: 100%; font-size: 21px; font-weight: 500; }

  /* eggs */
  .eggs { left: 4px; top: 1024px; width: 844px; height: 86px; background: var(--orange); text-align: center; }
  .eggs-line { left: 0; width: 100%; font-size: 22px; font-weight: 500; }

  /* contact */
  .contact { left: 4px; top: 1120px; width: 844px; height: 42px; background: var(--orange);
    display: flex; justify-content: center; align-items: center; gap: 64px;
    font-family: "Arimo", sans-serif; font-size: 18px; color: var(--leaf); }
  .contact-item { display: flex; align-items: center; gap: 8px; }
  .mark { width: 18px; height: 18px; background: var(--leaf); border-radius: 3px; }
  .mark.round { border-radius: 50%; }

  .band-left { left: 4px; top: 1172px; width: 422px; height: 16px; background: var(--lime); }
  .band-right { left: 426px; top: 1172px; width: 422px; height: 16px; background: var(--leaf); }
</style>
</head>
<body>
<div class="flyer">

  <div class="abs brand">
    <div class="brand-dot"></div>
    <div class="brand-name">Maple Hollow Farm</div>
  </div>
  <div class="abs tagline">Fresh - Local - Sustainable</div>

  <div class="abs frame-top"></div>
  <div class="abs frame-side"></div>
  <h1 class="abs title">Summer CSA</h1>

  <div class="abs photo photo-veg" role="img" aria-label="Photo of assorted fresh vegetables with an I love local tag"></div>
  <div class="abs photo alt photo-apple" role="img" aria-label="Photo of red apples with an I love local tag"></div>
  <div class="abs photo photo-greens" role="img" aria-label="Photo of lettuce growing in rows with a real organic veg tag"></div>
  <div class="abs photo alt photo-eggs" role="img" aria-label="Photo of brown free range eggs with a free range eggs tag"></div>

  <div class="abs rule"></div>

  <div class="abs about"></div>
  <ul class="abs about-list">
    <li>- Small family run produce and orchard farm</li>
    <li>-Local food and local produce</li>
    <li>-Serving our community</li>
    <li>-Using Organic / Biological best practises</li>
    <li>-Provide the best quality produce and fruit</li>
    <li>-non GMO seed and feed</li>
  </ul>

  <div class="abs offer">
    <div class="abs offer-num">18</div>
    <div class="abs offer-weeks">Weeks<br>produce</div>
    <div class="abs offer-delivery">Delivery Weekly</div>
    <div class="abs offer-dates">June 1<sup>St</sup> - October 11<sup>Th</sup></div>
  </div>

  <div class="abs season"></div>
  <h2 class="abs season-head">Here's what you could roughly expect for summer</h2>
  <p class="abs season-row" style="top:699px"><span class="month">June</span>: Broccoli-Cabbage-Sugar Snap Peas-Various Lettuces-Spinach-Kale-Swiss Chard-Beets</p>
  <p class="abs season-row" style="top:729px"><span class="month">July</span>: Broccoli-Lettuces-Kale-Snow Peas-Summer Squash-Zucchini-Cucumbers</p>
  <p class="abs season-row" style="top:759px; left:124px">Slicing Tomatoes-Cherry Tomatoes-Green Beans-October Beans-White&amp;Yellow Corn</p>
  <p class="abs season-row" style="top:790px">August : Same as July also - Various Bell Peppers-Sweet Peppers-Hot Peppers-Sweet Onions</p>
  <p class="abs season-row" style="top:826px">September/Mid October : Much the same as July/August along with several different varieties</p>
  <p class="abs season-row" style="top:856px; left:246px">of potatoes along with a few suprises</p>

  <div class="abs fruit">
    <h2 class="abs fruit-head">Summer Fruit options</h2>
    <p class="abs fruit-line" style="top:48px">starting in July : Peaches, Pears and Blackberries (and would run likely for 3-4 weeks)</p>
    <p class="abs fruit-line" style="top:84px">starting in September we will have several different Apple Varieties (Cooking and eating)</p>
  </div>

  <div class="abs eggs">
    <p class="abs eggs-line" style="top:12px">The eggs share would be a dozen free range, pastured large brown eggs weekly</p>
    <p class="abs eggs-line" style="top:48px">We also sell free range, pastured eggs</p>
  </div>

  <div class="abs contact">
    <span class="contact-item"><span class="mark"></span>maplehollowfarm</span>
    <span class="contact-item"><span class="mark round"></span>www.maplehollowfarm.com</span>
    <span class="contact-item"><span class="mark"></span>maplehollowfarm</span>
  </div>

  <div class="abs band-left"></div>
  <div class="abs band-right"></div>
</div>
</body>
</html>
```